VORNAX Technologies Catalogue Design

We want the existing catalogue design to be completely re designed to have a better theme, that is professional and dynamic. we want the existing pictures changed, it would be great to have some images of local UAE population engaging in the activities shown. most of the written content remains the same. No.1 what we believe is to be removed. Point No. 3 all the little logos need to be re designed.

Target Market(s)

residential and corporate clients

Industry/Entity Type

home automation, command centers, audio video systems, lighting control systems

Requirements
Must have
• Point No. 3 all the little logos need to be re designed. Overall theme of the catalogue should look very good.
Nice to have
• Good font. Color theme can be related to logo which is black grey and red. Red maybe little less, leaving it to the designer to decide. it would be nice to have the cover of the catalogue clean and elegant. I have added doc of a pattern in blue color, it would be nice if it can be used as theme in the entire catalogue either in grey or black color, not blue.

```html
<!DOCTYPE html>
<html lang="en">
<head>
<meta charset="utf-8">
<title>VORNAX Technologies – Home Automation</title>
<link rel="stylesheet" href="https://fonts.googleapis.com/css2?family=Arimo:wght@400;700&family=Roboto:wght@700;900&family=Source+Sans+3:wght@400&display=swap">
<style>
  :root {
    --title-ink: #1c1c1c;
    --accent-red: #c8161d;
    --body-ink: #262626;
    --hero-dark: #121212;
    --hero-mid: #3a3a3a;
    --hero-light: #8a8a8a;
    --band-dark: #1a1a1a;
    --band-mid: #3b3b3b;
    --tab-red: #c8161d;
    --seg-1: #c8161d;
    --seg-2: #2b2b2b;
    --seg-3: #7a7a7a;
    --seg-4: #e0353b;
    --seg-5: #4d4d4d;
    --seg-6: #a3a3a3;
    --label-ink: #111;
  }
  * { margin: 0; padding: 0; box-sizing: border-box; }
  html, body { width: 849px; height: 1200px; overflow: hidden; background: #fff; }
  .page { position: relative; width: 849px; height: 1200px; overflow: hidden; background: #fff; }

  .hero {
    position: absolute; left: 0; top: 0; width: 849px; height: 512px;
    background:
      radial-gradient(ellipse 220px 300px at 560px 260px, rgba(160,160,160,.45), transparent 70%),
      radial-gradient(ellipse 200px 160px at 330px 330px, rgba(196,150,120,.35), transparent 70%),
      linear-gradient(100deg, var(--hero-dark) 0%, var(--hero-mid) 45%, var(--hero-dark) 100%);
  }
  .hero-rule {
    position: absolute; left: 0; top: 512px; width: 849px; height: 4px; background: var(--accent-red);
  }

  .title {
    position: absolute; left: 57px; top: 572px;
    font-family: "Roboto", Arial, sans-serif; font-weight: 900;
    font-size: 52px; line-height: 54px; color: var(--title-ink); letter-spacing: 0.5px;
  }
  .title .accent { color: var(--accent-red); }

  .intro {
    position: absolute; left: 472px; top: 571px; width: 321px;
    font-family: "Source Sans 3", "Myriad Pro", sans-serif;
    font-size: 16.4px; line-height: 24.2px; color: var(--body-ink);
    text-align: justify; text-align-last: left;
  }

  .service-wheel { position: absolute; left: 60px; top: 695px; width: 376px; height: 376px; }
  .service-wheel text { font-family: "Arimo", Arial, sans-serif; fill: var(--label-ink); font-size: 17px; text-anchor: middle; }
  .service-wheel .hub-label { font-family: "Roboto", Arial, sans-serif; font-weight: 700; font-size: 20px; fill: #1c1c1c; }

  .footer-band {
    position: absolute; left: 0; top: 1137px; width: 849px; height: 63px;
    background:
      repeating-linear-gradient(60deg, rgba(255,255,255,.04) 0 30px, transparent 30px 60px),
      repeating-linear-gradient(-60deg, rgba(0,0,0,.12) 0 30px, transparent 30px 60px),
      linear-gradient(100deg, var(--band-dark), var(--band-mid) 50%, var(--band-dark));
  }
  .web-tab {
    position: absolute; left: 286px; top: 1151px; width: 277px; height: 49px;
    background: var(--tab-red); border-radius: 26px 26px 0 0;
    font-family: "Source Sans 3", sans-serif; color: #fff; font-size: 17px;
    text-align: center; line-height: 46px;
  }
</style>
</head>
<body>
<div class="page">
  <div class="hero" role="img" aria-label="Photo of a hand touching a grid of glowing app tiles with home, web, family, chart, cart, chat, person and wifi icons"></div>
  <div class="hero-rule"></div>

  <h1 class="title">HOME<br><span class="accent">AUTOMATION</span></h1>

  <p class="intro">Our Smart Home/Office Automation helps you to provide a fully integrated solution which can control Lighting, Shading, Security System, Audio Video Systems, Alarm Systems and Gate/Garage Control Systems from a single application. Our Integrated Solution helps you to create an intelligent Home with Enhanced Lifestyle Features. We are offering you a Wired and Wireless Solution depends on your choice of Integration. The solution can easily be integrated with Orvia Voice and Halden Hub for a complete Voice Guided Control of your Home/office. We are also providing you dedicated Touch panel controls, Mobile Applications and Wall Panel controls as per your choice. Wireless Solutions are suitable for those who wish to convert their already built Home into a fully Automated Home Using RF Solutions</p>

  <svg class="service-wheel" viewBox="-188 -188 376 376" aria-label="Home automation services wheel">
    <defs>
      <radialGradient id="discShade" cx="50%" cy="45%" r="55%">
        <stop offset="0%" stop-color="#ffffff"/>
        <stop offset="75%" stop-color="#f2f2f2"/>
        <stop offset="100%" stop-color="#d8d8d8"/>
      </radialGradient>
      <radialGradient id="hubShade" cx="45%" cy="35%" r="65%">
        <stop offset="0%" stop-color="#ffffff"/>
        <stop offset="70%" stop-color="#ececec"/>
        <stop offset="100%" stop-color="#c4c4c4"/>
      </radialGradient>
    </defs>
    <circle r="185" fill="url(#discShade)"/>
    <g fill="none" stroke-width="25">
      <path d="M-42.25,-73.18 A84.5,84.5 0 0 1 42.25,-73.18" stroke="var(--seg-1)"/>
      <path d="M42.25,-73.18 A84.5,84.5 0 0 1 84.5,0" stroke="var(--seg-2)"/>
      <path d="M84.5,0 A84.5,84.5 0 0 1 42.25,73.18" stroke="var(--seg-3)"/>
      <path d="M42.25,73.18 A84.5,84.5 0 0 1 -42.25,73.18" stroke="var(--seg-4)"/>
      <path d="M-42.25,73.18 A84.5,84.5 0 0 1 -84.5,0" stroke="var(--seg-5)"/>
      <path d="M-84.5,0 A84.5,84.5 0 0 1 -42.25,-73.18" stroke="var(--seg-6)"/>
    </g>
    <g fill="none" stroke-width="5" stroke-linejoin="miter">
      <polyline points="-48.5,-84 -92.5,-160" stroke="var(--seg-6)"/>
      <polyline points="48.5,-84 70,-118 80,-114 82,-134 94,-158" stroke="var(--seg-1)"/>
      <polyline points="97,0 125,0 137,13 150,0 185,0" stroke="var(--seg-2)"/>
      <polyline points="48.5,84 66,116 60,122 78,130 94,158" stroke="var(--seg-3)"/>
      <polyline points="-48.5,84 -64,112 -78,114 -72,134 -94,158" stroke="var(--seg-4)"/>
      <polyline points="-97,0 -128,0 -137,-11 -146,0 -185,0" stroke="var(--seg-5)"/>
    </g>
    <circle r="72" fill="url(#hubShade)" stroke="#c8c8c8" stroke-width="1"/>
    <text class="hub-label" x="0" y="-6">Home</text>
    <text class="hub-label" x="0" y="21">Automation</text>

    <text x="2" y="-153">Light /</text>
    <text x="2" y="-133">Dimming</text>
    <text x="2" y="-113">Control</text>

    <g transform="translate(121,-76) rotate(60)">
      <text x="0" y="-14">Curtain /</text>
      <text x="0" y="6">Shade</text>
      <text x="0" y="26">Control</text>
    </g>

    <g transform="translate(123,72) rotate(-60)">
      <text x="0" y="-4">AC</text>
      <text x="0" y="16">Control</text>
    </g>

    <text x="-4" y="126">Distributed</text>
    <text x="-4" y="146">Audio Video</text>
    <text x="-4" y="166">System</text>

    <g transform="translate(-122,70) rotate(60)">
      <text x="0" y="-4">CCTV &amp;</text>
      <text x="0" y="16">Intercom</text>
    </g>

    <g transform="translate(-125,-78) rotate(-60)">
      <text x="0" y="-4">Wifi &amp;</text>
      <text x="0" y="16">Telephone</text>
    </g>
  </svg>

  <div class="footer-band"></div>
  <div class="web-tab">www.vornaxtech.com</div>
</div>
</body>
</html>
```